card design for engineering consultancy

engineering drafting and project management company the provides drafting services for.
Electrical, Hydraulic, Mechanical, and Civil services
The company is called Q7R Services and logo is as attached
Information on card should be.
1. Logo
2.website : Q7RServices.example
3. email : info@Q7RServices.example
4. Phone: (+61) 400512836
5. Motto: Design - Document - Develop - Deliver

this card should be basically used for business identification only

Target Market(s)

electricians plumbers air conditioning installers and civil contractors

Industry/Entity Type

engineering, drafting, electrical, plumbing, airconditioning, civil

Contact Information for Business Card

1. Logo 2.website : Q7RServices.example 3. email : info@Q7RServices.example 4. Phone: (+61) 400512836 5. Motto: Design - Document - Develop - Deliver

Font styles to use
Serif

Requirements
Must have
• logo
Nice to have
• something inovative and different that makes it stand out from being just another business card

```html
<!DOCTYPE html>
<html lang="en">
<head>
<meta charset="utf-8">
<title>Q7R Services — Business Card</title>
<link rel="stylesheet" href="https://fonts.googleapis.com/css2?family=Montserrat:wght@400;500;700;800&display=swap">
<style>
  :root {
    --bg: #23282b;
    --card-white: #ffffff;
    --card-back-a: #f4f4f4;
    --card-back-b: #dcdcdc;
    --ink: #3b3b3d;
    --ink-soft: #555558;
    --red: #e0202a;
    --grey-band: #3d3f42;
    --divider: #3b3b3d;
  }
  * { box-sizing: border-box; margin: 0; padding: 0; }
  html, body { width: 1200px; height: 800px; overflow: hidden; }
  body {
    background: var(--bg);
    font-family: "Montserrat", sans-serif;
    position: relative;
  }
  .card {
    position: absolute;
    top: 250px;
    width: 520px;
    height: 300px;
    border-radius: 22px;
    overflow: hidden;
  }
  .card--front { left: 50px; background: var(--card-white); }
  .card--back { left: 630px; background: linear-gradient(135deg, var(--card-back-a), var(--card-back-b)); }

  .front-decor { position: absolute; inset: 0; width: 520px; height: 300px; }

  .contact-block { position: absolute; left: 38px; top: 52px; }
  .company-title {
    color: var(--red);
    font-weight: 800;
    font-size: 22px;
    letter-spacing: 0.2px;
    text-transform: uppercase;
  }
  .title-rule { width: 40px; height: 3px; background: var(--red); margin: 8px 0 8px; }
  .motto { color: var(--ink-soft); font-size: 12px; line-height: 17px; font-weight: 500; }
  .contact-list { list-style: none; margin-top: 14px; }
  .contact-item {
    display: flex; align-items: center; gap: 10px;
    color: var(--ink-soft); font-size: 12px; font-weight: 500;
    margin-bottom: 8px;
  }
  .contact-icon { width: 20px; height: 20px; flex: none; }

  .divider {
    position: absolute; left: 268px; top: 40px;
    width: 2px; height: 150px; background: var(--divider);
  }

  .brand-mark {
    position: absolute; display: flex; align-items: center; gap: 10px;
  }
  .brand-mark--front {
    left: 269px; right: 0; top: 40px; height: 150px;
    justify-content: center;
  }
  .brand-square { width: 20px; height: 20px; background: var(--red); flex: none; }
  .brand-name {
    color: var(--ink); font-weight: 700; font-size: 19px;
    letter-spacing: 0.5px; text-transform: uppercase; white-space: nowrap;
  }

  .back-pattern {
    position: absolute; inset: 0;
    background: radial-gradient(circle at 50% 50%, rgba(255,255,255,0.55), rgba(200,200,200,0.35));
  }
  .brand-mark--back { left: 50%; top: 50%; transform: translate(-50%, -50%); }
  .brand-mark--back .brand-square { width: 22px; height: 22px; }
  .brand-mark--back .brand-name { font-size: 26px; }
</style>
</head>
<body>
  <section class="card card--front" aria-label="Business card front">
    <svg class="front-decor" viewBox="0 0 520 300" aria-hidden="true">
      <polygon fill="var(--grey-band)" points="0,284 112,284 98,300 0,300"/>
      <polygon fill="var(--red)" points="128,300 182,250 322,250 372,206 520,206 520,222 382,222 334,266 196,266 160,300"/>
      <polygon fill="var(--grey-band)" points="408,196 424,184 520,184 520,196"/>
      <polygon fill="var(--red)" points="214,300 236,280 300,280 278,300"/>
    </svg>

    <div class="contact-block">
      <h1 class="company-title">Q7R Services</h1>
      <div class="title-rule"></div>
      <p class="motto">Design - Document<br>Develop - Deliver</p>
      <ul class="contact-list">
        <li class="contact-item">
          <svg class="contact-icon" viewBox="0 0 20 20" aria-hidden="true">
            <circle cx="10" cy="10" r="10" fill="var(--red)"/>
            <rect x="5" y="6.5" width="10" height="7" fill="none" stroke="#fff" stroke-width="1.4"/>
            <polyline points="5,6.5 10,10.5 15,6.5" fill="none" stroke="#fff" stroke-width="1.4"/>
          </svg>
          <span>info@Q7RServices.example</span>
        </li>
        <li class="contact-item">
          <svg class="contact-icon" viewBox="0 0 20 20" aria-hidden="true">
            <circle cx="10" cy="10" r="10" fill="var(--red)"/>
            <path d="M7 5.5 L8.8 5.5 L9.6 8 L8.4 9 Q9.3 11 11 11.8 L12 10.6 L14.5 11.4 L14.5 13.2 Q9.5 14 6.5 8.5 Q6.3 6.5 7 5.5 Z" fill="#fff"/>
          </svg>
          <span>(+61) 400512836</span>
        </li>
        <li class="contact-item">
          <svg class="contact-icon" viewBox="0 0 20 20" aria-hidden="true">
            <circle cx="10" cy="10" r="10" fill="var(--red)"/>
            <circle cx="10" cy="10" r="5" fill="none" stroke="#fff" stroke-width="1.3"/>
            <ellipse cx="10" cy="10" rx="2.2" ry="5" fill="none" stroke="#fff" stroke-width="1.1"/>
            <line x1="5" y1="10" x2="15" y2="10" stroke="#fff" stroke-width="1.1"/>
          </svg>
          <span>Q7RServices.example</span>
        </li>
      </ul>
    </div>

    <div class="divider"></div>

    <div class="brand-mark brand-mark--front">
      <span class="brand-square"></span>
      <span class="brand-name">Q7R Services</span>
    </div>
  </section>

  <section class="card card--back" aria-label="Business card back">
    <div class="back-pattern" role="img" aria-label="Faint repeating brand pattern background"></div>
    <div class="brand-mark brand-mark--back">
      <span class="brand-square"></span>
      <span class="brand-name">Q7R Services</span>
    </div>
  </section>
</body>
</html>
```